Home Services- Spring Clean Options

Brightwell Crew provides a variety of Home Services- focused on cleaning & improving the exterior of the home:

 Power Washing- driveways, sidewalks, patios, decks, fence
 Fence Staining- make fence look new with variety of staining colors
 Gutter cleaning- important to make sure have proper Water Drainage
 Gutter Guard Installation- prevent damage to roof and house by keeping debris out of gutters and water flowing.
 Window Washing- our exterior washing team and reach the highest windows
 Landscape& Patio Lights- highlight areas for beauty and safety
Updates

We are are almost finished. Just please make sure you pay attention to the wording and grammer in Red thx

Target Market(s)

Middle to Upper level Home Owners (especially women)

Industry/Entity Type

Cleaning Services

Font styles to use
Serif
Sans Serif

Requirements
Must have
• Not be Cluttered- Clean friendly, professional look. Focus on the Professional

Info@GoBrightwellCrew.com
972-648-0000
Nice to have
• Pictures of services- these are just examples
Should not have
• Bigger and bolder Services & Specials. Want to Show all the Services we offer but do Not use too much detail- don't want it to look "cluttered"

```html
<!DOCTYPE html>
<html lang="en">
<head>
<meta charset="utf-8">
<title>Brightwell Crew – Cleaning & Improving the Exterior</title>
<link href="https://fonts.googleapis.com/css2?family=Lato:ital,wght@0,400;0,700;0,900;1,700&display=swap" rel="stylesheet">
<style>
  :root{
    --page:#e4e5e7;
    --navy:#151b27;
    --navy-deep:#0e1119;
    --green:#6cc24a;
    --green-dark:#4e9a2e;
    --white:#ffffff;
    --muted:#d9dde3;
  }
  *{box-sizing:border-box;margin:0;padding:0}
  html,body{width:1200px;height:1200px;overflow:hidden}
  body{background:var(--page);font-family:"Lato",Arial,sans-serif}
  .flyer{position:absolute;left:200px;top:35px;width:800px;height:1130px;background:var(--navy);overflow:hidden}
  .hero-photo{position:absolute;left:230px;top:0;width:570px;height:660px;
    background:linear-gradient(160deg,#3f6b34 0%,#5a7d45 30%,#8d8576 60%,#6d675d 80%,#2f3a2b 100%)}
  .shapes{position:absolute;left:0;top:0}
  .thumb{position:absolute;left:62px;width:208px;height:170px;border-radius:18px;border:4px solid var(--white)}
  .thumb--lights{top:58px;background:linear-gradient(180deg,#2a3346 0%,#5a4a36 60%,#c08a4a 100%)}
  .thumb--washing{top:252px;background:linear-gradient(180deg,#c9c3b6 0%,#8aa072 55%,#4e7a34 100%)}
  .thumb--windows{top:446px;background:linear-gradient(150deg,#e8ecef 0%,#b8c3cc 50%,#6e8aa0 100%)}
  .headline{position:absolute;left:448px;top:640px;color:var(--white);font-weight:900;font-size:38px;line-height:40px;text-transform:uppercase;letter-spacing:.5px}
  .headline-rule{position:absolute;left:432px;top:640px;width:3px;height:118px;background:var(--white)}
  .intro{position:absolute;left:40px;top:784px;width:720px;color:var(--green);font-weight:700;font-size:19px;line-height:24px}
  .services{position:absolute;list-style:none}
  .services--left{left:40px;top:848px;width:360px}
  .services--right{left:430px;top:848px;width:340px}
  .service{border-left:2px solid var(--green);padding-left:10px;margin-bottom:10px}
  .service-name{color:var(--green);font-weight:700;font-size:14px;text-transform:uppercase;line-height:17px}
  .service-desc{color:var(--muted);font-size:13px;line-height:16px}
  .contact{position:absolute;left:418px;top:990px;width:382px;height:76px;background:var(--green);padding:8px 22px;color:var(--navy-deep)}
  .contact-line{font-weight:700;font-size:13px;letter-spacing:1.5px;line-height:17px}
  .contact-phone{font-weight:900;font-size:24px;letter-spacing:1px;line-height:28px}
  .edge-stripe{position:absolute;left:0;top:1096px;width:800px;height:18px;background:var(--green)}
</style>
</head>
<body>
<main class="flyer">
  <div class="hero-photo" role="img" aria-label="Family dining on a stone patio while a man grills at an outdoor kitchen"></div>
  <svg class="shapes" width="800" height="1130" viewBox="0 0 800 1130" aria-hidden="true">
    <path d="M230,0 V120 Q250,40 360,0 Z" fill="var(--navy)"/>
    <path d="M0,700 L230,690 C400,600 560,560 800,600 L800,1130 L0,1130 Z" fill="var(--navy-deep)"/>
    <path d="M0,0 H300 V650 Q300,690 260,690 H50 Q20,690 20,660 V60 Q120,20 300,0 Z" fill="var(--green)"/>
    <path d="M0,0 H300 Q120,20 20,60 L0,70 Z" fill="var(--navy)"/>
  </svg>
  <div class="thumb thumb--lights" role="img" aria-label="Uplit trees along a fence at night"></div>
  <div class="thumb thumb--washing" role="img" aria-label="Pressure washer cleaning a sidewalk by a lawn"></div>
  <div class="thumb thumb--windows" role="img" aria-label="Man washing an exterior window with a squeegee"></div>

  <div class="headline-rule"></div>
  <h1 class="headline">Cleaning &amp;<br>Improving<br>The Exterior</h1>

  <p class="intro">Brightwell Crew Provides A Variety Of Home Services- Focused On Cleaning &amp; Improving The Exterior Of The Home:</p>

  <ul class="services services--left">
    <li class="service"><div class="service-name">Power Washing</div><div class="service-desc">driveways, sidewalks, patios, decks, fence</div></li>
    <li class="service"><div class="service-name">Fence Staining</div><div class="service-desc">make fence look new with variety of staining colors</div></li>
    <li class="service"><div class="service-name">Gutter Cleaning</div><div class="service-desc">important to make sure have proper Water Drainage</div></li>
    <li class="service"><div class="service-name">Window Washing</div><div class="service-desc">our exterior washing team and reach the highest windows</div></li>
  </ul>
  <ul class="services services--right">
    <li class="service"><div class="service-name">Gutter Guard Installation</div><div class="service-desc">prevent damage to roof and house by keeping debris out of gutters and water flowing.</div></li>
    <li class="service"><div class="service-name">Landscape &amp; Patio Lights</div><div class="service-desc">highlight areas for beauty and safety</div></li>
  </ul>

  <div class="contact">
    <div class="contact-line">Info@GoBrightwellCrew.com</div>
    <div class="contact-line">www.GoBrightwellCrew.com</div>
    <div class="contact-phone">972-555-0148</div>
  </div>
  <div class="edge-stripe"></div>
</main>
</body>
</html>
```